Website for Torvane Capital - investment banking firm

We have a corporate identity (thanks to Ravella/48213) and want to extend that into a website design.  See the attached zipped files.
We have software folks in-house to do the coding.
See the attached Project Brief & Notes for more details.  Don't worry about the actual text - lorem ipsum will be fine.
The server will be Apache.
Thank you!
Leopold

```html
<!DOCTYPE html>
<html lang="en">
<head>
<meta charset="utf-8">
<title>Torvane Capital</title>
<link rel="stylesheet" href="https://fonts.googleapis.com/css2?family=Ubuntu:wght@300;400;500&family=Cinzel:wght@400;700&family=Crimson+Text&display=swap">
<style>
  :root {
    --brand-blue: #0a56a4;
    --brand-blue-dark: #0b4a8e;
    --text-grey: #555a60;
    --soft-grey: #8a8d91;
    --rule: #e4e6e8;
    --link-light: #a9c3e2;
    --white: #ffffff;
    --map-grey: #f1f2f3;
  }
  * { margin: 0; padding: 0; box-sizing: border-box; }
  html, body { width: 1200px; height: 1032px; overflow: hidden; background: var(--white); }
  body { position: relative; font-family: "Ubuntu", sans-serif; color: var(--text-grey); }

  .site-header { position: absolute; top: 0; left: 0; width: 1200px; height: 70px; z-index: 3; }
  .brand { position: absolute; left: 200px; top: 20px; display: flex; align-items: center; gap: 10px; }
  .brand-square { width: 22px; height: 22px; background: var(--brand-blue); }
  .brand-name { font-family: "Cinzel", serif; font-weight: 400; font-size: 23px; color: var(--brand-blue); letter-spacing: 0.5px; }

  .main-nav { position: absolute; right: 203px; top: 27px; display: flex; font-size: 10.5px; text-transform: uppercase; }
  .main-nav a { color: var(--text-grey); text-decoration: none; }
  .main-nav a.current { color: var(--brand-blue); }
  .main-nav .sep { margin: 0 10px; color: var(--soft-grey); }

  .hero { position: absolute; top: 0; left: 0; width: 1200px; height: 472px; }
  .hero-map { position: absolute; left: 416px; top: 76px; width: 704px; height: 396px;
    background: radial-gradient(ellipse at 55% 45%, #eceef0 0%, var(--map-grey) 55%, #fafafa 100%); }
  .hero-photo { position: absolute; left: 96px; top: 84px; width: 418px; height: 388px;
    background: linear-gradient(180deg, #c9b8a6 0%, #2a3142 42%, #1c2232 100%); border-radius: 160px 160px 0 0; }
  .region-pin { position: absolute; display: flex; align-items: flex-start; gap: 6px; font-size: 16px; color: #6b6e72; }
  .region-pin svg { display: block; }

  .tagline-band { position: absolute; top: 472px; left: 0; width: 1200px; height: 81px; background: var(--brand-blue);
    display: flex; align-items: center; justify-content: center; }
  .tagline-band h1 { font-family: "Cinzel", serif; font-weight: 700; font-size: 24px; color: var(--white); letter-spacing: -0.3px; }

  .intro { position: absolute; top: 578px; left: 190px; width: 820px; text-align: center; font-weight: 300; font-size: 13px; line-height: 17px; color: var(--text-grey); }

  .offices { position: absolute; top: 658px; left: 200px; width: 800px; height: 110px; }
  .office { position: absolute; top: 0; width: 180px; text-align: center; }
  .office-title { display: flex; align-items: center; justify-content: center; gap: 6px; height: 48px; }
  .office-title h2 { font-family: "Cinzel", serif; font-weight: 400; font-size: 19px; color: #60636a; }
  .office address { font-style: normal; font-size: 10px; line-height: 12.5px; margin-top: 8px; color: var(--text-grey); }
  .office-divider { position: absolute; top: 18px; width: 1px; height: 90px; background: var(--rule); }

  .contact-rule { position: absolute; top: 821px; left: 0; width: 1200px; height: 1px; background: var(--rule); }
  .contact-strip { position: absolute; top: 852px; left: 0; width: 1200px; height: 34px; }
  .contact-item { position: absolute; display: flex; align-items: center; gap: 9px; font-family: "Crimson Text", serif; font-size: 18px; color: #8d9094; }

  .site-footer { position: absolute; top: 919px; left: 0; width: 1200px; height: 113px; background: var(--brand-blue-dark); }
  .footer-heading { position: absolute; left: 201px; top: 24px; font-size: 10.5px; font-weight: 500; color: var(--white); }
  .footer-nav { position: absolute; left: 201px; top: 56px; display: flex; font-size: 10.5px; text-transform: uppercase; }
  .footer-nav a { color: var(--link-light); text-decoration: none; }
  .footer-nav .sep { margin: 0 9px; color: var(--link-light); }
  .footer-brand { position: absolute; right: 200px; top: 42px; display: flex; align-items: center; gap: 8px; }
  .footer-brand .brand-square { background: #8aa6c8; width: 18px; height: 18px; }
  .footer-brand .brand-name { color: #9fb6d2; font-size: 18px; }
  .copyright { position: absolute; left: 820px; width: 200px; top: 87px; text-align: center; font-size: 11px; color: var(--white); }
</style>
</head>
<body>

<header class="site-header">
  <div class="brand"><span class="brand-square"></span><span class="brand-name">Torvane Capital</span></div>
  <nav class="main-nav">
    <a class="current" href="#">Home</a><span class="sep">/</span>
    <a href="#">About</a><span class="sep">/</span>
    <a href="#">Services</a><span class="sep">/</span>
    <a href="#">Current Engagements</a><span class="sep">/</span>
    <a href="#">Completed Transactions</a>
  </nav>
</header>

<section class="hero">
  <div class="hero-map" role="img" aria-label="Faint grey world map"></div>
  <div class="hero-photo" role="img" aria-label="Photo of two business professionals standing with arms crossed"></div>
  <div class="region-pin" style="left:471px; top:118px;">
    <svg width="30" height="48" viewBox="0 0 30 48"><path d="M15 1C7 1 1 7 1 15c0 10 14 32 14 32s14-22 14-32C29 7 23 1 15 1z" fill="#0a56a4"/><circle cx="15" cy="15" r="7" fill="none" stroke="#fff" stroke-width="3"/><circle cx="15" cy="15" r="2.5" fill="#fff"/></svg>
    <span>North America</span>
  </div>
  <div class="region-pin" style="left:934px; top:150px;">
    <svg width="25" height="40" viewBox="0 0 30 48"><path d="M15 1C7 1 1 7 1 15c0 10 14 32 14 32s14-22 14-32C29 7 23 1 15 1z" fill="#0a56a4"/><circle cx="15" cy="15" r="7" fill="none" stroke="#fff" stroke-width="3"/><circle cx="15" cy="15" r="2.5" fill="#fff"/></svg>
    <span style="margin-top:-6px;">Asia-Pacific</span>
  </div>
</section>

<div class="tagline-band"><h1>GLOBAL, PROFESSIONAL, TRUSTED … OR DISCIPLINED / EFFECTIVE?</h1></div>

<p class="intro">Torvane Capital is an independent investment bank working for buyers in a number of industries. We utilize exceptional technology in finding companies to meet our client’s search criteria. We will not waste a buyer’s time, a seller’s time, or our own time.</p>

<section class="offices">
  <div class="office" style="left:-3px;">
    <div class="office-title">
      <svg width="26" height="44" viewBox="0 0 26 44"><path d="M13 1C6 1 1 6 1 13c0 9 12 30 12 30s12-21 12-30C25 6 20 1 13 1z" fill="#e9eaeb" stroke="#cfd1d3"/><circle cx="13" cy="13" r="9" fill="#d9261c"/></svg>
      <h2>CHINA</h2>
    </div>
    <address>Hong Kong: Suite 1408 Harbourline<br>Tower 12 - 18 Marlow Road East<br>Kestrel Bay, Hong Kong</address>
  </div>
  <div class="office-divider" style="left:183px;"></div>
  <div class="office" style="left:191px;">
    <div class="office-title">
      <svg width="26" height="44" viewBox="0 0 26 44"><path d="M13 1C6 1 1 6 1 13c0 9 12 30 12 30s12-21 12-30C25 6 20 1 13 1z" fill="#e9eaeb" stroke="#cfd1d3"/><circle cx="13" cy="13" r="9" fill="#f7f7f7"/><circle cx="13" cy="13" r="4.5" fill="#d9261c"/></svg>
      <h2>JAPAN</h2>
    </div>
    <address>Hong Kong: Suite 1408 Harbourline<br>Tower 12 - 18 Marlow Road East<br>Kestrel Bay, Hong Kong</address>
  </div>
  <div class="office-divider" style="left:388px;"></div>
  <div class="office" style="left:401px;">
    <div class="office-title">
      <svg width="26" height="44" viewBox="0 0 26 44"><path d="M13 1C6 1 1 6 1 13c0 9 12 30 12 30s12-21 12-30C25 6 20 1 13 1z" fill="#e9eaeb" stroke="#cfd1d3"/><circle cx="13" cy="13" r="9" fill="#c4283a"/><path d="M4 13h18" stroke="#fff" stroke-width="2"/><path d="M5 9h16M5 17h16" stroke="#fff" stroke-width="1.5"/><path d="M4 13a9 9 0 0 1 9-9v9z" fill="#2b3f8c"/></svg>
      <h2>AMERICA</h2>
    </div>
    <address>Hong Kong: Suite 1408 Harbourline<br>Tower 12 - 18 Marlow Road East<br>Kestrel Bay, Hong Kong</address>
  </div>
  <div class="office-divider" style="left:596px;"></div>
  <div class="office" style="left:612px;">
    <div class="office-title" style="margin-top:5px;">
      <svg width="26" height="44" viewBox="0 0 26 44"><path d="M13 1C6 1 1 6 1 13c0 9 12 30 12 30s12-21 12-30C25 6 20 1 13 1z" fill="#e9eaeb" stroke="#cfd1d3"/><circle cx="13" cy="13" r="9" fill="#f7f7f7"/><path d="M4 13a9 9 0 0 1 4-7.5v15A9 9 0 0 1 4 13zM22 13a9 9 0 0 0-4-7.5v15a9 9 0 0 0 4-7.5z" fill="#d9261c"/><path d="M13 8l2 4h-4z M11 12h4v4h-4z" fill="#d9261c"/></svg>
      <h2>CANADA</h2>
    </div>
    <address style="margin-top:3px;">Hong Kong: Suite 1408 Harbourline<br>Tower 12 - 18 Marlow Road East<br>Kestrel Bay, Hong Kong</address>
  </div>
</section>

<div class="contact-rule"></div>
<section class="contact-strip">
  <div class="contact-item" style="left:201px; top:2px;">
    <svg width="25" height="28" viewBox="0 0 25 28" fill="none" stroke="#0a56a4" stroke-width="2"><path d="M2 11l10.5-8 10.5 8v15H2z"/><path d="M2 11l10.5 8 10.5-8M2 26l8-8M23 26l-8-8"/><path d="M6 8h13v6" /></svg>
    <span>Email - info@torvanecapital.com</span>
  </div>
  <div class="contact-item" style="left:526px; top:0;">
    <svg width="30" height="28" viewBox="0 0 30 28" fill="#0a56a4"><path d="M2 9c0-4 6-7 13-7s13 3 13 7v2h-6V8c-2-1-4-1.5-7-1.5S10 7 8 8v3H2z"/><circle cx="11" cy="15" r="1.8"/><circle cx="15" cy="15" r="1.8"/><circle cx="19" cy="15" r="1.8"/><circle cx="11" cy="19.5" r="1.8"/><circle cx="15" cy="19.5" r="1.8"/><circle cx="19" cy="19.5" r="1.8"/><circle cx="11" cy="24" r="1.8"/><circle cx="15" cy="24" r="1.8"/><circle cx="19" cy="24" r="1.8"/></svg>
    <span>Telephone - 555-210-3874</span>
  </div>
  <div class="contact-item" style="left:836px; top:0;">
    <svg width="28" height="28" viewBox="0 0 28 28" fill="none" stroke="#0a56a4" stroke-width="2"><path d="M7 10V2h11l3 3v5"/><rect x="2" y="10" width="24" height="10" rx="1"/><rect x="7" y="17" width="14" height="9"/><path d="M10 21h8M10 24h8"/></svg>
    <span style="margin-left:-4px;">Fax - 555-210-3874</span>
  </div>
</section>

<footer class="site-footer">
  <div class="footer-heading">QUICK LINKS</div>
  <nav class="footer-nav">
    <a href="#">Home</a><span class="sep">/</span>
    <a href="#">About</a><span class="sep">/</span>
    <a href="#">Services</a><span class="sep">/</span>
    <a href="#">Current Engagements</a><span class="sep">/</span>
    <a href="#">Completed Transactions</a>
  </nav>
  <div class="footer-brand"><span class="brand-square"></span><span class="brand-name">Torvane Capital</span></div>
  <div class="copyright">Copyright Torvane Capital.</div>
</footer>

</body>
</html>
```